Book Cover needed - Disinformation and fake news

I need a book cover (front, back, spine) for the 1st edition of a book entitled ‘Marea Silenciosa’ (Means – Silent Tide) and subtitled ‘Ecos perdidos entre relojes de arena’ (Means - Echoes lost among hourglasses) (inverted commas not to be part of the title and subtitle). The author is ‘Tomás Ferreira’. The finished size of the paperback version will be 5.25" x 8". There will be paperback and e-book versions, so 2 covers will need to be provided: one for the e-book version just with the front cover, and the full book cover for the paperback version.
The final number of pages is expected to be in the region of 350-500 pages. Text for the back cover is down below, and at the bottom of the back cover should have space for the ISBN bar code on the right. The books will be published with RLV - Orvita, so should follow their indications for any specification needed.
The topics discussed include disinformation, fake news, psychological operations. Feel free to design the cover based on those. The design should be original and not include any stock images that have been created by someone else or may require obtaining a copyright license to use.
Back Cover Text (spacing should be respected) :
Ministerio de la verdad, desinformación, “fake news”... en los últimos años nos hemos visto envueltos en una discusión pública rodeados de estos términos sin terminar de entender exactamente qué significan y lo que es peor, sin saber que realmente nos rodean desde que el hombre es hombre.
En esta obra el autor busca acercanos al mundo de la Marea Silenciosa, aquellas operaciones que buscan influir sobre el comportamiento de la población. Sin hacer uso de un lenguaje excesivamente técnico relata como la evolución de la naturaleza de la guerra a los parámetros del siglo XXI promueve un enfoque del conflicto que no supone un uso de la fuerza tradicional. ¿Para qué atacar las instituciones de un país de forma directa, cuando puedes fomentar el conflicto social entre grupos antagónicos y desestabilizar sin realizar un solo disparo?
¿Cómo razona el ser humano? ¿Son nuestras ideas tan nuestras como creemos? ¿Por qué importa tanto el uso preciso del lenguaje a la hora de comunicarnos?, ¿Cómo nos afectan las razones y emociones de los demás? ¿Por qué tendemos a prestar mayor atención a argumentos que encajen con nuestras propias ideas? ¿Cómo nos afecta la conversación en redes sociales?
Armados con el conocimiento que reside en este libro, quizás, seamos menos susceptibles de caer bajo la influencia de grupos con intereses espurios.
General public with an interest on disinformation - fake news

```html
<!DOCTYPE html>
<html lang="es">
<head>
<meta charset="utf-8">
<title>Marea Silenciosa — Tomás Ferreira</title>
<link rel="stylesheet" href="https://fonts.googleapis.com/css2?family=Oswald:wght@600;700&family=Roboto+Condensed:wght@700&display=swap">
<style>
  :root {
    --page-bg: #ffffff;
    --cover-grey: #bdbdbd;
    --cover-grey-light: #d6d6d6;
    --ink-red: #c1272d;
    --ink-black: #151515;
    --ink-white: #ffffff;
    --figure-white: #f1f1f1;
  }
  html, body {
    margin: 0;
    padding: 0;
    width: 1200px;
    height: 960px;
    overflow: hidden;
    background: var(--page-bg);
  }
  .canvas {
    position: relative;
    width: 1200px;
    height: 960px;
  }
  .cover {
    position: absolute;
    left: 311px;
    top: 40px;
    width: 578px;
    height: 880px;
    overflow: hidden;
    background: radial-gradient(ellipse at 50% 45%, var(--cover-grey-light) 0%, var(--cover-grey) 75%);
  }
  .title-row {
    position: absolute;
    margin: 0;
    white-space: nowrap;
    font-family: "Oswald", "Arial Narrow", sans-serif;
    font-weight: 700;
    font-size: 118px;
    line-height: 1;
    letter-spacing: -0.01em;
    text-transform: uppercase;
    transform: scaleY(1.08);
    transform-origin: left top;
  }
  .title-row .red { color: var(--ink-red); }
  .title-row .black { color: var(--ink-black); }
  .row-1 { top: 40px;  left: -210px; }
  .row-2 { top: 140px; left: -40px; }
  .row-3 { top: 400px; left: -120px; }
  .row-4 { top: 490px; left: -330px; }
  .row-5 { top: 580px; left: -250px; }
  .row-6 { top: 665px; left: -90px; }
  .row-7 { top: 735px; left: 260px; }

  .subtitle {
    position: absolute;
    top: 262px;
    left: 0;
    width: 100%;
    margin: 0;
    text-align: center;
    font-family: "Roboto Condensed", "Arial Narrow", sans-serif;
    font-weight: 700;
    font-size: 27px;
    line-height: 1.38;
    letter-spacing: 0.14em;
    text-transform: uppercase;
  }
  .subtitle .line-light { display: block; color: var(--ink-white); }
  .subtitle .line-dark { display: block; color: var(--ink-black); }

  .figure-area {
    position: absolute;
    left: 0;
    top: 0;
    width: 578px;
    height: 880px;
  }
  .author {
    position: absolute;
    bottom: 46px;
    left: 0;
    width: 100%;
    margin: 0;
    text-align: center;
    font-family: "Oswald", "Arial Narrow", sans-serif;
    font-weight: 600;
    font-size: 30px;
    letter-spacing: 0.12em;
    color: var(--ink-black);
    text-transform: uppercase;
  }
</style>
</head>
<body>
<main class="canvas">
  <section class="cover" aria-label="Portada del libro Marea Silenciosa">
    <h1 class="title-row row-1"><span class="black">Silenciosa </span><span class="red">Marea Silenciosa</span></h1>
    <p class="title-row row-2" aria-hidden="true"><span class="black">Silenciosa </span><span class="red">Marea</span></p>

    <p class="subtitle">
      <span class="line-light">Ecos perdidos</span>
      <span class="line-dark">entre relojes de arena</span>
    </p>

    <p class="title-row row-3" aria-hidden="true"><span class="red">Marea Silenciosa </span><span class="black">Marea</span></p>
    <p class="title-row row-4" aria-hidden="true"><span class="black">Silenciosa </span><span class="red">Marea Silenciosa</span></p>
    <p class="title-row row-5" aria-hidden="true"><span class="red">Silenciosa </span><span class="black">Marea Silenciosa</span></p>
    <p class="title-row row-6" aria-hidden="true"><span class="black">Marea Silenciosa</span></p>
    <p class="title-row row-7" aria-hidden="true"><span class="red">Marea</span></p>

    <svg class="figure-area" viewBox="0 0 578 880" role="img" aria-label="Ilustración: silueta blanca de una persona con una tecla roja luminosa con una bomba en la cabeza">
      <defs>
        <radialGradient id="figure-glow" cx="0.5" cy="0.12" r="0.6">
          <stop offset="0" stop-color="#f6d4d4"/>
          <stop offset="0.25" stop-color="var(--figure-white)"/>
          <stop offset="1" stop-color="#e4e4e4"/>
        </radialGradient>
      </defs>
      <path d="M140 880 L140 420 Q140 370 190 370 L388 370 Q438 370 438 420 L438 880 Z" fill="url(#figure-glow)"/>
    </svg>

    <p class="author">Tomás Ferreira</p>
  </section>
</main>
</body>
</html>
```